Swimming Pool Service Website needed!!!

Hi Everyone! Thanks for looking at my contest. I PROMISE to provide excellent feedback during this process.

I am starting a new swimming pool business cleaning company in San Diego, California and would like your help in making it similar to one of these two websites that are already functioning.

http://www.brightlagoonworks.example/services-repair.html

http://tidemarkaquacare.example/commercial-pool-cleaning.php

I like these two because they are easy to read, classy, sophisticated and have nice pictures of really clean & clear pools.

I really like the blue on white color format.

I do not have a logo, but the name of my company is GLIMMERWAVE POOL SERVICE.

My tag line is: Water so pure, it sparkles like a summer sky. (does not need to have the quotes around "in"...maybe just italics for this word IN?) You decide for me.

I would like to have a logo designed that incorporates some sort of easy to read letters. I do not want cursive (handwriting) letters. I thought about having a "reflection" of letters (mirror image), but think that this will be hard to read from far away. Maybe you can surprise me and come up with an idea that works using the a mirror image....but I'm not sure. I was leaning toward plain old BLOCK letters as I think it would be easy to read on my truck.

I would like to have 5 pages on my website:
1) Home
2) About Us (Know Your Poolman) / Why Hire Us
3) Services Offered
4) FAQ's
5) Contact

I am looking for a fully-functioning website (coded). Upon selection of the design winner, I am offering to increase the budget/payment by $100-$125 for the coding of all the pages. So anyone looking at participating in this contest, should be willing and able to provide the coding to the webpages that i've requested.

Target Market(s)

Upper middle-class homeowners who have a pool

Industry/Entity Type

Pool Service

Number of Pages Required

5+ page

Font styles to use
Serif

Colors
0455a3
3276b5
85acd3
85cae6
ffffff
33a6d7
0592cd

Requirements
Must have
• The Home page must have this picture highlighted in the top of the page:
• http://www.mesawaterpro.example/
• Must have pictures of some high-end pools. Any that you can find on the internet are wonderful.
• Must have a table on the right of the home page that mentions the service areas that we go to:
• • Carmel Valley (92130)
• • Del Mar (92014)
• • Rancho Santa Fe (92067)
• • Solana Beach (92075)
• • Santaluz (92127)
• • Cardiff (92007)
• • Encinitas (92024)
• • Carlsbad (92009, 92008)
• • La Jolla (92037)
• • Pacific Beach (92109)
• • Mira Mesa (92126)
• • Sorrento Valley (92121)
• • Clairemont (92117)
• • Rancho Bernardo (92127, 92128)
• • Rancho Penasquitos (92129)
• • Poway (92064)
• •
Nice to have
• Maybe incorporate some pictures of some kids (or families) playing in pools on the Why Hire Us page?
• I also like the feel of this website, but posting this page just for reference so you can get a feel more of what I like:
• http://www.crestlinepool.example/
• I like the FAQ's page from this website. I like how you can click on the question and then it pops up with the answer. http://www.dunewoodpoolcare.example/pool-spa-fountain-faqs/

```html
<!DOCTYPE html>
<html lang="en">
<head>
<meta charset="utf-8">
<title>Glimmerwave Pool Services</title>
<link href="https://fonts.googleapis.com/css2?family=Arimo:wght@400;700&family=Cinzel:wght@400;600&family=Roboto+Condensed:ital,wght@0,400;1,400&family=Ubuntu:wght@500;700&display=swap" rel="stylesheet">
<style>
:root{
  --navy:#1f4f8f;
  --deep:#0455a3;
  --mid:#3276b5;
  --sky:#33a6d7;
  --panel:#3aa2dd;
  --field:#b9dff4;
  --footer:#2a86c4;
  --text:#555;
  --line:#b5b5b5;
  --white:#fff;
}
*{box-sizing:border-box;margin:0;padding:0}
html,body{width:989px;height:1200px;overflow:hidden}
body{position:relative;font-family:"Arimo",Arial,sans-serif;color:var(--text);background:#1a6aa8}
.ocean{position:absolute;inset:0;background:linear-gradient(160deg,#2c86c6 0%,#1563a6 40%,#2a8ccc 70%,#0f5a9c 100%)}
.page{position:absolute;left:130px;top:0;width:726px;height:1200px;background:var(--white)}
.abs{position:absolute}
.brand{left:6px;top:34px;font-family:"Cinzel",serif;font-weight:600;font-size:16.5px;color:var(--navy);letter-spacing:.3px;white-space:nowrap}
.call{left:555px;top:14px;display:flex;gap:7px;align-items:center}
.call small{display:block;font-family:"Cinzel",serif;font-size:10.5px;color:var(--mid);font-weight:600}
.call b{display:block;font-family:"Ubuntu",sans-serif;font-size:16px;color:var(--deep)}
.nav{top:63px;left:256px;display:flex;font-size:11.3px;color:#222}
.nav span{padding:0 10px;border-right:1px solid #ccc;line-height:12px}
.nav span:last-child{border:0}
.nav .on{border-bottom:2px solid var(--deep);padding-bottom:5px}
.hero{left:0;top:106px;width:726px;height:290px;background:linear-gradient(135deg,#a38d6d 0%,#6fb3c4 30%,#5aa6bd 60%,#c0ab8a 100%);border-radius:3px}
.tag{left:170px;top:344px;width:386px;height:38px;background:rgba(90,90,90,.72);color:#fff;font-family:"Roboto Condensed",sans-serif;font-style:italic;font-size:18px;text-align:center;line-height:38px;white-space:nowrap}
.inquiry{left:490px;top:98px;width:192px;height:210px;background:var(--panel);border-radius:3px;padding:14px 13px;box-shadow:0 1px 3px rgba(0,0,0,.3)}
.inquiry h2{font-family:"Ubuntu",sans-serif;font-size:17px;color:#fff;margin-bottom:8px}
.field{background:var(--field);height:17px;margin-bottom:6px;font-size:8px;color:#555;padding:3px 7px}
.field.tall{height:57px}
.submit{display:inline-block;background:var(--navy);color:#fff;font-family:"Ubuntu",sans-serif;font-size:10.5px;padding:5px 7px;border-radius:2px;margin-top:0}
.dots{left:344px;top:403px;display:flex;gap:3px}
.dots i{width:5px;height:5px;border-radius:50%;background:#999}
.dots i:first-child{background:var(--navy)}
.card{top:428px;width:218px;height:90px;border:1px solid #999;border-radius:6px;padding:9px 12px 0 66px}
.card svg{position:absolute;left:6px;top:10px}
.card h3{font-family:"Roboto Condensed",sans-serif;font-weight:400;font-size:14px;color:var(--deep);margin-bottom:4px}
.card p{font-size:9.3px;line-height:14px;color:#555}
.more{text-decoration:underline;color:#222;font-size:9.8px}
.card .more{position:absolute;right:12px;bottom:5px}
h2.sec{font-family:"Cinzel",serif;font-weight:600;font-size:14.5px;color:var(--deep);border-bottom:1px dashed var(--line);padding-bottom:3px}
.copy{font-size:9.4px;line-height:14.3px;color:#555}
.vline{left:476px;top:546px;width:1px;height:530px;background:#ddd}
ul.tri{list-style:none}
ul.tri li{position:relative;padding-left:12px;font-size:9.3px;color:#555}
ul.tri li:before{content:"";position:absolute;left:0;top:3px;border-left:4px solid var(--sky);border-top:4px solid transparent;border-bottom:4px solid transparent}
.areas li{line-height:15.2px}
.svc li{line-height:14.4px;margin-bottom:2.3px}
.quote{font-size:9.5px;line-height:15.4px;color:#333}
.qm{font-family:Georgia,serif;font-size:30px;color:#999;line-height:10px;vertical-align:-12px;font-weight:700}
.footer{left:-2px;top:1110px;width:731px;height:90px;background:var(--footer);color:#fff}
.fnav{left:14px;top:16px;display:flex;font-size:9.6px}
.fnav span{padding:0 8px;border-right:1px solid #fff;line-height:11px}
.fnav span:first-child{padding-left:0;width:42px}
.fnav span:last-child{border:0}
.finfo{left:20px;top:40px;font-size:10px;font-weight:700}
.follow{left:458px;top:16px;font-size:10px}
.soc{left:458px;top:31px;display:flex;gap:8px}
.soc i{width:18px;height:18px;border-radius:3px;background:#5aa4d8;border:1px solid #8cc4ea}
.fbrand{left:592px;top:24px;width:140px;text-align:center;font-family:"Cinzel",serif;font-weight:600;font-size:14.5px;line-height:17px}
.copyr{left:0;top:73px;width:731px;text-align:center;font-size:8.2px}
</style>
</head>
<body>
<div class="ocean" role="img" aria-label="Open blue ocean water background"></div>
<div class="page">
  <div class="abs brand">GLIMMERWAVE POOL SERVICES</div>
  <div class="abs call">
    <svg width="24" height="24" viewBox="0 0 24 24"><circle cx="12" cy="12" r="11" fill="none" stroke="#3276b5" stroke-width="1.5"/><path d="M9 6c-2 1-2 4 0 8s4 5 6 4l-2-3-1.3.6c-1-1-2-3-2.2-4.6L10.6 9z" fill="#3276b5"/></svg>
    <div><small>Call Us Today</small><b>858-555-0172</b></div>
  </div>
  <div class="abs nav"><span class="on">Home</span><span>About Us</span><span>Services Offered</span><span>FAQ's</span><span>Why Hire Us</span><span>Contact Us</span></div>

  <div class="abs hero" role="img" aria-label="Photo of a clean backyard swimming pool with stone edging, a potted palm and a water feature"></div>
  <div class="abs tag">Water so pure, it sparkles like a summer sky</div>
  <div class="abs inquiry">
    <h2>Quick Inquiry</h2>
    <div class="field">Name</div>
    <div class="field">Email</div>
    <div class="field">Mobile</div>
    <div class="field tall">Questions / Comments</div>
    <span class="submit">Submit</span>
  </div>
  <div class="abs dots"><i></i><i></i><i></i><i></i><i></i></div>

  <div class="abs card" style="left:14px">
    <svg width="50" height="46" viewBox="0 0 50 46"><path d="M2 18 17 4l15 14h-4v16H6V18z" fill="#1f4f8f"/><rect x="13" y="24" width="7" height="10" fill="#fff"/><path d="M30 24v20M38 24v20M30 30h8M30 36h8" stroke="#1f4f8f" stroke-width="2"/><path d="M26 40q3-2 6 0t6 0 6 0M26 44q3-2 6 0t6 0 6 0" stroke="#33a6d7" stroke-width="1.5" fill="none"/></svg>
    <h3>Residential Services</h3>
    <p>Glimmerwave Pool Service offers maintenance and repairs for all residential pools.</p>
    <span class="more">Read More</span>
  </div>
  <div class="abs card" style="left:254px">
    <svg width="50" height="46" viewBox="0 0 50 46"><path d="M4 34V18h6V8h4v26zM16 34V22h8v12z" fill="#1f4f8f"/><path d="M28 22v16M36 22v16M28 28h8" stroke="#1f4f8f" stroke-width="2"/><path d="M2 38q4-2 8 0t8 0 8 0 8 0 8 0M2 43q4-2 8 0t8 0 8 0 8 0 8 0" stroke="#33a6d7" stroke-width="1.5" fill="none"/></svg>
    <h3>Commercial Services</h3>
    <p>we do it all! Health Clubs, Schools, Hotels, Motels, Apartments, Condominiums</p>
    <span class="more">Read More</span>
  </div>
  <div class="abs card" style="left:492px">
    <svg width="36" height="36" viewBox="0 0 24 24"><circle cx="12" cy="12" r="11" fill="none" stroke="#1f4f8f" stroke-width="1.3"/><path d="M9 6c-2 1-2 4 0 8s4 5 6 4l-2-3-1.3.6c-1-1-2-3-2.2-4.6L10.6 9z" fill="#1f4f8f"/></svg>
    <h3>Quick Inquiry</h3>
    <p>Please call or E-Mail us with any questions about our pool service, or to schedule a free pool...</p>
    <span class="more">Read More</span>
  </div>

  <div class="abs" style="left:13px;top:546px;width:428px">
    <h2 class="sec">Welcome to Glimmerwave Pool Services</h2>
    <p class="copy" style="margin-top:16px">At Glimmerwave Pool Service, we understand that your pool is an important investment. Whether it's part of your business or in your backyard, it needs to be well taken care of to ensure its longevity and your peace of mind. At Glimmerwave Pool Service, we pride ourselves in setting the standard in our industry. What sets us apart from our competition is our commitment to excellence. Our exceptional service and competitive price make us the clear choice for your pool service needs.</p>
    <p class="copy" style="margin-top:14px">Glimmerwave Pool Service has been providing spectacular pool &amp; spa cleaning and maintenance service for over 7 years. Our technicians are professionally trained and are committed to providing outstanding customer service through our honest...</p>
    <p style="margin-top:6px"><span class="more">Read More</span></p>
  </div>

  <div class="abs" style="left:13px;top:763px;width:428px">
    <h2 class="sec">Service Areas That We Go To:</h2>
  </div>
  <ul class="abs tri areas" style="left:14px;top:795px"><li>Carmel Valley (92130)</li><li>Del Mar (92014)</li><li>Rancho Santa Fe (92067)</li><li>Solana Beach (92075)</li><li>Santaluz (92127)</li><li>Cardiff (92007)</li></ul>
  <ul class="abs tri areas" style="left:168px;top:795px"><li>Mira Mesa (92126)</li><li>Encinitas (92024)</li><li>Carlsbad (92009, 92008)</li><li>La Jolla (92037)</li><li>Pacific Beach (92109)</li></ul>
  <ul class="abs tri areas" style="left:315px;top:795px"><li>Sorrento Valley (92121)</li><li>Clairemont (92117)</li><li>Rancho Bernardo (92127, 92128)</li><li>Rancho Penasquitos (92129)</li><li>Poway (92064)</li></ul>

  <div class="abs" style="left:13px;top:916px;width:428px">
    <h2 class="sec">Customer Reviews</h2>
    <p class="quote" style="margin-top:9px"><span class="qm">&ldquo;</span>&nbsp; Working with Dale is terrific. His education and professional background sets him apart from all the other pool cleaners. He has excellent communication with us and he shows up when he says he will. Glimmerwave is the only pool care company I have ever recommended to my friends <span class="qm">&rdquo;</span></p>
    <p class="quote" style="margin-top:10px"><span class="qm">&ldquo;</span>&nbsp; I was looking for a pool service company and I'm so glad I found Glimmerwave! Dale, the owner, is an honest business man. Don't go anywhere else! You'll be surprised at what a great communicator Dale is and the service that he does is awesome! <span class="qm">&rdquo;</span></p>
    <p style="margin-top:8px"><span class="more">Read More</span></p>
  </div>

  <div class="abs vline"></div>

  <div class="abs" style="left:497px;top:546px;width:205px">
    <h2 class="sec">Services Offered</h2>
    <p class="copy" style="margin-top:11px;line-height:12.4px">Glimmerwave Pool Service is a full service company. We cover the complete spectrum of regular service and repair. From start-ups to restoring swampy pools, repairing or replacing equipment, Glimmerwave does it all</p>
    <ul class="tri svc" style="margin-top:6px">
      <li>Swimming Pool and Spa Cleaning</li><li>Install and repair lighting</li><li>New Pool and Spa Start Ups</li><li>Leak Detection &amp; Salt System Conversions</li><li>Troubleshoot and Repair pumps, filters, heaters and heat exchangers</li><li>Fountain Cleaning and Service</li><li>Tile Cleaning &amp; Restoration</li><li>Licensed and Bonded Swimming Pool Technicians</li><li>CPO (Certified Pool Operator) Insured</li><li>Low Rates for Repairs, Maintenance, Cleaning</li><li>Reliable &amp; affordable pool &amp; spa maintenance</li><li>Friendly assistance from the staff</li><li>Brushing walls and tile cleaning</li><li>Salt water system maintenance</li><li>Pool leakage detection and repairs</li><li>Noisy pool motor repairs</li><li>Prompt swimming pool cleaning each week Vacuuming pool floor and steps</li><li>Eliminating leaves and debris</li><li>Cleaning out debris in skimmer and pool pump basket</li><li>Making your pool and spa crystal clear with balanced chemicals</li>
    </ul>
  </div>
  <span class="abs more" style="left:665px;top:1068px">Read More</span>

  <div class="abs footer">
    <div class="abs fnav"><span>Home</span><span>About Us</span><span>Services Offered</span><span>FAQ's</span><span>Why Hire Us</span><span>Contact Us</span></div>
    <div class="abs finfo">Street Name City Name State Zipcode &nbsp;|&nbsp; Phone: 858-555-0172</div>
    <div class="abs follow">Follow Us On</div>
    <div class="abs soc"><i></i><i></i><i></i></div>
    <div class="abs fbrand">GLIMMERWAVE<br>POOL SERVICES</div>
    <div class="abs copyr">Copyright &copy; 2015, GlimmerwavePoolServices.example | All Rights Reserved.</div>
  </div>
</div>
</body>
</html>
```